Gin Bottle label

Hi, I would like a design based on a traditional, Vintage, Victorian type label.
The product is 'Thistle & Marrowroot Gin'
It will be 50cl and 40% vol.
The Gin will be dark brown in colour and attached is the types of bottle and a few ideas of the styles I like.
Many Thanks

```html
<!DOCTYPE html>
<html lang="en">
<head>
<meta charset="UTF-8">
<title>Thistle &amp; Marrowroot Gin – Bottle Label</title>
<link rel="stylesheet" href="https://fonts.googleapis.com/css2?family=Arvo:wght@700&family=Playfair+Display:wght@700&family=Kalam:wght@300&family=Open+Sans:wght@600&display=swap">
<style>
  :root {
    --page: #ffffff;
    --outline: #0d1733;
    --copper: #a2632a;
    --copper-light: #cd8a4e;
    --mahogany: #5a2510;
    --walnut: #481b05;
    --cream-line: #e6ddd6;
    --ampersand: #9e8e88;
    --muted-text: #a89a94;
    --ornament: #9a5a26;
    --hatch: #6a3417;
  }
  html, body {
    margin: 0;
    padding: 0;
    width: 1200px;
    height: 1200px;
    overflow: hidden;
    background: var(--page);
  }
  .label-canvas {
    display: block;
    width: 1200px;
    height: 1200px;
  }
  .frame-outer { fill: var(--copper); stroke: var(--outline); stroke-width: 4; }
  .frame-band { fill: var(--mahogany); }
  .frame-rule { fill: var(--copper); stroke: var(--cream-line); stroke-width: 2; }
  .frame-field { fill: var(--walnut); }
  .ornament-area { fill: url(#ornament-glow); }
  .ribbon { fill: var(--copper); stroke: var(--mahogany); stroke-width: 2; }
  .ribbon-fold { fill: #7e461b; stroke: var(--mahogany); stroke-width: 2; }
  .ribbon-text {
    font-family: "Open Sans", sans-serif;
    font-weight: 600;
    font-size: 30px;
    fill: var(--cream-line);
    letter-spacing: 1px;
  }
  .ampersand {
    font-family: "Playfair Display", serif;
    font-weight: 700;
    font-size: 290px;
    fill: var(--ampersand);
  }
  .product-name {
    font-family: "Arvo", serif;
    font-weight: 700;
    font-size: 62px;
    fill: var(--copper-light);
    stroke: #1e0a02;
    stroke-width: 1.5;
    paint-order: stroke;
  }
  .detail-script {
    font-family: "Kalam", cursive;
    font-weight: 300;
    font-size: 36px;
    fill: var(--muted-text);
  }
  .hatch-rule { fill: var(--hatch); }
</style>
</head>
<body>
<svg class="label-canvas" viewBox="0 0 1000 1000" xmlns="http://www.w3.org/2000/svg">
  <defs>
    <path id="label-shape" d="M205,262 H240 V245 Q268,238 272,200 V145 H305 C330,60 420,22 505,22 C590,22 680,60 705,145 H740 V200 Q744,238 772,245 V262 H807 V735 H772 V752 Q744,760 740,798 V850 H705 C680,935 590,972 505,972 C420,972 330,935 305,850 H272 V798 Q268,760 240,752 V735 H205 Z"/>
    <radialGradient id="ornament-glow" cx="50%" cy="50%" r="50%">
      <stop offset="0%" stop-color="#9a5a26" stop-opacity="0.75"/>
      <stop offset="60%" stop-color="#8a4d1f" stop-opacity="0.4"/>
      <stop offset="100%" stop-color="#481b05" stop-opacity="0"/>
    </radialGradient>
  </defs>

  <g class="label-frame">
    <use href="#label-shape" class="frame-outer"/>
    <use href="#label-shape" class="frame-band" transform="translate(505 497) scale(0.955 0.965) translate(-505 -497)"/>
    <use href="#label-shape" class="frame-rule" transform="translate(505 497) scale(0.905 0.93) translate(-505 -497)"/>
    <use href="#label-shape" class="frame-field" transform="translate(505 497) scale(0.895 0.922) translate(-505 -497)"/>
  </g>

  <ellipse class="ornament-area" cx="507" cy="150" rx="128" ry="70" role="img" aria-label="Symmetrical floral filigree ornament"/>

  <g class="maker-ribbon">
    <path class="ribbon-fold" d="M365,262 L400,248 L418,262 L398,292 Z"/>
    <path class="ribbon-fold" d="M645,262 L610,250 L592,266 L628,290 Z"/>
    <path class="ribbon" d="M395,262 Q505,220 615,262 L600,300 Q505,268 410,300 Z"/>
    <text class="ribbon-text" x="508" y="292" text-anchor="middle">COMPANY</text>
  </g>

  <g class="scroll-flourishes" role="img" aria-label="Curled scroll flourishes framing the product name">
    <ellipse class="ornament-area" cx="358" cy="366" rx="78" ry="28"/>
    <ellipse class="ornament-area" cx="654" cy="366" rx="78" ry="28"/>
    <ellipse class="ornament-area" cx="358" cy="612" rx="78" ry="28"/>
    <ellipse class="ornament-area" cx="654" cy="612" rx="78" ry="28"/>
  </g>

  <text class="ampersand" x="522" y="582" text-anchor="middle">&amp;</text>

  <g class="product-title">
    <text class="product-name" x="502" y="470" text-anchor="middle">Thistle</text>
    <text class="product-name" x="505" y="553" text-anchor="middle" textLength="490" lengthAdjust="spacingAndGlyphs">Marrowroot Gin</text>
  </g>

  <text class="detail-script" x="502" y="644" text-anchor="middle">40% vol</text>
  <text class="detail-script" x="508" y="708" text-anchor="middle">50 cl</text>

  <rect class="hatch-rule" x="330" y="736" width="350" height="10"/>

  <ellipse class="ornament-area" cx="507" cy="842" rx="128" ry="72" role="img" aria-label="Symmetrical floral filigree ornament"/>
</svg>
</body>
</html>
```